依頼詳細
展示会で配るチラシデザインを作成してください。
デザインやセンスで選びたいと思っております。
気兼ねなく、ご応募ください。
概要・特徴はあくまでも参考まで、ほかの文章・キャッチフレーズがあれば使ってください。
記載項目
社名、電話番号、URL、キャッチコピー、会社ロゴ
サイズ
A4
ページ数
両面
希望イメージ
シンプル 複雑
単色 カラフル
暗い 明るい
日常 高級
遊び心 厳粛
未来的 伝統的
女性的 男性的
希望する色
青系、ほかの色合いも出してくれても良いです
納品ファイル
• イラストレーター形式 (.ai)
補足説明
表面にインパクトのあるデザインで裏に詳細をデザインでお願いします。
色合い、デザイン、文章、キャッチフレーズ など案があれば出してください。
A4両面デザインで
概要・特徴に書いていることも記載項目で文章を抜粋して頂いても大丈夫です。
追記にて写真も添付させて頂きます。
宜しくお願い致します。
会社情報
ミルテ株式会社
〒530-0047 大阪市北区西天満4-5-6
TEL 06-6318-2450
FAX 06-6318-2451
info@mirte-example.jp
宜しくお願い致します。
■ 選んだ理由

全案良かったのでコメントは差し控えさせていただきます。

■ 提案者全員のお礼・コメント

悩みに悩んだあげく当選させて頂きました。
コンペに参加して頂いた皆様には大変感謝しております。
全案良かったので採用できませんでした方には申し訳ありませんでした。
コンペ・直接依頼をすることもあるかと思いますが宜しくお願い致します。

```html
<!DOCTYPE html>
<html lang="ja">
<head>
<meta charset="utf-8">
<title>ミルテ株式会社 天然キハダマグロ</title>
<link href="https://fonts.googleapis.com/css2?family=M+PLUS+1p:wght@400;700;800&family=Noto+Sans+JP:wght@400;700;900&display=swap" rel="stylesheet">
<style>
:root{
  --sky:#6fb4e3;
  --sea:#1a5f9e;
  --navy:#0d2d6b;
  --red:#d61a1f;
  --orange:#f08c1a;
  --white:#ffffff;
  --text:#333333;
  --tuna-red:#b3262c;
  --footer-blue:#1d4f9c;
}
*{margin:0;padding:0;box-sizing:border-box}
html,body{width:854px;height:1200px;overflow:hidden;background:#fff}
body{font-family:"Noto Sans JP",sans-serif;color:var(--text)}
.flyer{position:relative;width:854px;height:1200px;overflow:hidden}
.scene{position:absolute;left:0;top:0;width:854px;height:985px;
  background:linear-gradient(180deg,#b4dcf4 0%,var(--sky) 30%,#3a86c6 62%,var(--sea) 100%)}
.tuna-art{position:absolute;right:0;top:0;width:330px;height:190px;
  background:radial-gradient(ellipse at 60% 40%,#c9d3dc 0%,#8c9aa8 50%,rgba(140,154,168,0) 75%)}
.tuna-bottom{position:absolute;left:0;top:880px;width:180px;height:100px;
  background:radial-gradient(ellipse at 40% 50%,#c8d1da 0%,#7f8e9c 50%,rgba(127,142,156,0) 75%)}
.headline{position:absolute;left:26px;top:18px;width:660px;
  font-family:"M PLUS 1p",sans-serif;font-weight:800;line-height:1.2;white-space:nowrap;
  text-shadow:0 0 3px #fff,0 0 3px #fff,0 0 4px #fff,2px 2px 0 #fff,-2px -2px 0 #fff,2px -2px 0 #fff,-2px 2px 0 #fff}
.headline span{display:block}
.headline .l1{color:var(--navy);font-size:32px}
.headline .l2{color:var(--red);font-size:44px;margin-top:2px}
.headline .l3{color:var(--navy);font-size:36px;margin-top:2px}
.lead{position:absolute;left:30px;top:250px;color:var(--white);font-weight:900;
  font-size:21px;line-height:1.35;text-shadow:0 1px 3px rgba(0,0,0,.45)}
.point{position:absolute;border-radius:50%;background:rgba(255,255,255,.95);
  display:flex;flex-direction:column;align-items:center;text-align:center;overflow:hidden}
.point .num{width:52px;height:52px;border-radius:50%;background:var(--orange);color:#fff;
  font-weight:900;font-size:28px;display:flex;align-items:center;justify-content:center;
  border:3px solid #fff;flex:none}
.point h3{color:var(--red);font-weight:900;font-size:20px;line-height:1.3;margin:8px 0 6px}
.point p{font-size:12px;line-height:1.6;color:var(--text);width:74%}
.point .photo{width:100%;flex:1;margin-top:10px}
.p1{left:38px;top:318px;width:318px;height:318px;padding-top:26px}
.p2{left:494px;top:180px;width:330px;height:330px;padding-top:22px}
.p3{left:48px;top:642px;width:330px;height:330px;padding-top:24px}
.p4{left:470px;top:560px;width:356px;height:356px;padding-top:26px}
.fish-meat{background:linear-gradient(135deg,#d94a4f,var(--tuna-red) 60%,#7e1a1f)}
.factory{background:linear-gradient(180deg,#8fb7d6,#4d6f8c)}
.recruit{position:absolute;left:0;top:985px;width:854px;height:60px;background:var(--red);
  color:#fff;text-align:center}
.recruit h2{font-family:"M PLUS 1p",sans-serif;font-weight:800;font-size:34px;line-height:60px}
.footer{position:absolute;left:0;top:1045px;width:854px;height:155px;background:#fff;padding:18px 30px}
.brand{display:flex;align-items:center;gap:8px;color:var(--footer-blue);font-weight:900;font-size:26px}
.brand .mark{width:22px;height:22px;border-radius:50%;background:var(--footer-blue)}
.company{margin-top:6px;font-weight:700;font-size:20px;color:var(--navy)}
.company .url{font-size:11px;font-weight:400;color:var(--text);display:block}
.contact{position:absolute;left:250px;top:18px;font-size:12px;color:var(--text);line-height:1.5}
.contact .row{display:flex;align-items:center;gap:8px;margin-top:4px}
.contact .tag{background:var(--footer-blue);color:#fff;font-size:11px;font-weight:700;padding:1px 6px}
.contact .big{font-size:22px;font-weight:900;color:var(--footer-blue)}
.contact .mail{font-size:19px;font-weight:700;color:var(--footer-blue)}
.side-photos{position:absolute;right:24px;top:14px;width:140px;height:130px;
  display:flex;flex-direction:column;gap:4px}
.side-photos .ph{flex:1;background:linear-gradient(135deg,#7aa6c8,#365f85)}
.side-photos .cap{font-size:10px;text-align:center;color:var(--text)}
</style>
</head>
<body>
<div class="flyer">
  <div class="scene" role="img" aria-label="青空と海の写真"></div>
  <div class="tuna-art" role="img" aria-label="跳ねるキハダマグロのイラスト"></div>
  <div class="tuna-bottom" role="img" aria-label="マグロのイラスト"></div>

  <h1 class="headline">
    <span class="l1">新鮮で美味しく高品質の</span>
    <span class="l2">バリ島産天然生キハダマグロを</span>
    <span class="l3">確実にお客様へお届けする!</span>
  </h1>

  <div class="lead">私たちがお届けする<br>天然キハダマグロの美味しさのヒミツ</div>

  <section class="point p2">
    <div class="num">2</div>
    <h3>最短で水揚げ3日後に<br>生鮮品で食卓に並ぶ</h3>
    <p>水揚げしたその日のうちに加工し、空輸で日本へ直送。冷凍せずに生のまま、鮮度を保ってお届けします。</p>
    <div class="photo fish-meat" role="img" aria-label="キハダマグロの切り身の写真"></div>
  </section>

  <section class="point p1">
    <div class="num">1</div>
    <h3>キハダマグロの<br>本当の美味しさを知っている</h3>
    <p>産地を知り尽くしたスタッフが、旬の時期と漁場を見極めて仕入れています。鮮度と脂のりにこだわり、本当に美味しいマグロだけを選んでお届けします。</p>
  </section>

  <section class="point p4">
    <div class="num">4</div>
    <h3>4つの加工工場が稼働、<br>一日500kgまで納品可能</h3>
    <p>現地の4つの加工工場が連携し、衛生管理を徹底。一日最大500kgまでの出荷に対応でき、大口のご注文にも安心です。</p>
    <div class="photo factory" role="img" aria-label="加工工場での作業風景の写真"></div>
  </section>

  <section class="point p3">
    <div class="num">3</div>
    <h3>一本釣り手釣りで<br>高品質なキハダマグロを提供</h3>
    <p>一本ずつ丁寧に釣り上げるため、魚体が傷つかず身質が良好。品質の高いマグロを安定して提供します。</p>
    <div class="photo factory" role="img" aria-label="漁船と一本釣りの写真"></div>
  </section>

  <div class="recruit">
    <h2>販路拡大に伴い、取引先様大募集!</h2>
  </div>

  <footer class="footer">
    <div class="brand"><span class="mark"></span>MIRTE</div>
    <div class="company">ミルテ株式会社<span class="url">http://www.mirte-example.jp</span></div>
    <div class="contact">
      <div>〒530-0047 大阪市北区西天満4-5-6</div>
      <div class="row"><span class="tag">TEL</span><span class="big">06-6318-2450</span><span class="tag">FAX</span><span class="big">06-6318-2451</span></div>
      <div class="row"><span class="tag">E-MAIL</span><span class="mail">info@mirte-example.jp</span></div>
    </div>
    <div class="side-photos">
      <div class="ph" role="img" aria-label="輸入風景の写真"></div>
      <div class="ph" role="img" aria-label="現地加工工場の写真"></div>
      <div class="cap">輸入風景・現地加工工場</div>
    </div>
  </footer>
</div>
</body>
</html>
```